Dealer Price List June 2013

Simple, PDF price list for our customers. Word doc will be provided. Needs to be formatted nice and a design added. Product pictures will be provided. Only 2-3 pics per page plus company logo. 1 page, double sided flyer. Must be PDF only.
Updates

Additionally product details can be found at www.paperfinch.comĀ 

Industry/Entity Type

It Company

```html
<!DOCTYPE html>
<html lang="en">
<head>
<meta charset="utf-8">
<title>Paper Finch 2013 Reseller Pricing</title>
<link rel="stylesheet" href="https://fonts.googleapis.com/css2?family=Roboto+Condensed:wght@400;700&display=swap">
<style>
:root{
  --backdrop:#e6e6e6;
  --paper:#ffffff;
  --ink:#1c1c1c;
  --muted:#444;
  --red:#e0201f;
  --blue-head:#6f86c4;
  --row-a:#dfe3f3;
  --row-b:#eef0f8;
  --cyan-head:#14a6e0;
  --cyan-a:#c6e6f6;
  --cyan-b:#e2f2fb;
  --gold:#f6c20f;
  --gold-light:#fbe6a2;
  --green-head:#7cbb42;
  --green-a:#d3e8b8;
  --green-b:#e9f3dc;
  --terms-top:#fde7b6;
  --terms-bottom:#f7c98d;
  --brown:#a34a2a;
  --band:#e4e4e4;
  --brand:#2b2320;
}
*{box-sizing:border-box;margin:0;padding:0}
html,body{width:1200px;height:1000px;overflow:hidden}
body{background:var(--backdrop);font-family:"Roboto Condensed",Arial,sans-serif;color:var(--ink);position:relative}
.sheet{position:absolute;top:140px;width:505px;height:715px;background:var(--paper)}
.sheet-front{left:60px}
.sheet-back{left:628px}

.brand{position:absolute;left:0;right:0;top:188px;text-align:center;font-weight:700;font-size:30px;letter-spacing:3px;color:var(--brand)}
.sheet-front .brand{top:50px}
.title{position:absolute;left:0;right:0;top:144px;text-align:center;color:var(--red);font-weight:700;font-size:20.5px}
.effective{position:absolute;left:0;right:0;top:173px;text-align:center;font-size:8.5px}
.freight{position:absolute;left:0;right:0;top:183px;text-align:center;font-size:11px}

.price-table{position:absolute;left:49px;width:412px;border-collapse:collapse;font-size:10px}
.price-table th{color:#fff;font-weight:700;font-size:10.5px;height:14px;padding:0 6px 0 18px;text-align:left}
.price-table th.price,.price-table td.price{text-align:right}
.price-table td{height:14.35px;padding:0 6px 0 18px;white-space:nowrap}
.price-table td b{font-weight:700}
.price-table small{font-size:8px}
.price-table td.price b{font-size:11px}
.front-table{top:203px}
.front-table th{background:var(--blue-head)}
.front-table tr:nth-child(odd) td{background:var(--row-a)}
.front-table tr:nth-child(even) td{background:var(--row-b)}

.product-shot{position:absolute}
.shot-ball{left:50px;top:125px;width:42px;height:48px;background:radial-gradient(circle at 50% 55%,#efe7d4 0 35%,#c9b58a 36%,#f3eee4 70%)}
.shot-basketball{left:100px;top:70px;width:90px;height:100px;background:linear-gradient(180deg,#d9dde2,#b9653a 55%,#2a2a2a)}
.shot-sleeves{left:330px;top:78px;width:130px;height:92px;background:linear-gradient(135deg,#3a3a3a,#9aa0a6 55%,#e6c86a)}
.sheet-back .brand{top:115px;left:200px;right:auto;width:130px;font-size:17px;letter-spacing:1.5px}

.back-top{top:202px}
.back-top th{background:var(--cyan-head)}
.back-top tr:nth-child(odd) td{background:var(--cyan-a)}
.back-top tr:nth-child(even) td{background:var(--cyan-b)}
.price-table td.code{padding-left:18px;width:1%}
.bills{top:297px}
.bills tr:first-child td{background:var(--gold)}
.bills tr:last-child td{background:var(--gold-light)}
.cases{top:334px}
.cases th{background:var(--green-head);text-align:center}
.cases tr:nth-child(odd) td{background:var(--green-a)}
.cases tr:nth-child(even) td{background:var(--green-b)}
.cases td.code{width:44px;padding-right:0}
.cases td{padding-left:8px}

.terms{position:absolute;left:49px;top:497px;width:412px;height:39px;background:linear-gradient(180deg,var(--terms-top),var(--terms-bottom));text-align:center;font-size:7.5px;line-height:9px;padding-top:3px}
.terms b{font-weight:700}
.terms .label{color:var(--brown)}

.company{position:absolute;left:0;right:0;top:546px;text-align:center}
.company-name{font-weight:700;font-size:19px;color:var(--brown)}
.company-line{font-size:10.5px;color:var(--muted);line-height:11px}
.payment-band{position:absolute;left:0;right:0;top:608px;height:42px;background:var(--band);display:flex;justify-content:center;gap:13px;padding-top:5px}
.pay-badge{width:60px;height:33px;background:#fff;font-size:10px;font-weight:700;display:flex;align-items:center;justify-content:center;color:var(--brand)}
.ship-note{position:absolute;left:0;right:0;top:656px;text-align:center;font-weight:700;font-size:10px}
.fine-print{position:absolute;left:0;right:0;top:668px;text-align:center;font-size:7px;color:var(--muted)}
</style>
</head>
<body>

<section class="sheet sheet-front">
  <div class="brand">PAPER FINCH</div>
  <h1 class="title">2013 Reseller Pricing - $500 Minimum Order</h1>
  <p class="effective">Effective June 1, 2013 &nbsp;Mix and Match all products</p>
  <p class="freight">FREIGHT INCLUDED TO COMMERCIAL ADDRESSES &nbsp;$29 Residential Surcharge</p>
  <table class="price-table front-table">
    <tr><th>Description</th><th class="price">Price</th></tr>
    <tr><td><b>Top-Load 3x4 Clear Card Holder</b> <small>(Case/1,000)</small></td><td class="price"><b>$37.50</b>/case</td></tr>
    <tr><td><b>Top-Load 3x4 “Rookie” Gold or Color Edge</b> <small>25/1,000/18 lbs.</small></td><td class="price"><b>$45</b>/case</td></tr>
    <tr><td><b>Top-Load 3x4 1.5mm 60 Pt.</b> <small>(Case/1,000)</small></td><td class="price"><b>$65</b>/case</td></tr>
    <tr><td><b>Top-Load 3x4 2.5mm 100 Pt.</b> <small>(Case/500)</small></td><td class="price"><b>$48</b>/case</td></tr>
    <tr><td><b>Top-Load 3x4 3.5mm 140 Pt.</b> <small>(Case/500)</small></td><td class="price"><b>$69</b>/case</td></tr>
    <tr><td><b>Top-Load 3x4 5mm 190 Pt.</b> <small>(Case/250)</small></td><td class="price"><b>$45</b>/case</td></tr>
    <tr><td><b>Top-Load 3x4 7mm 240 Pt.</b> <small>(Case/250)</small></td><td class="price"><b>$49</b>/case</td></tr>
    <tr><td><b>Top-Load 4x6 Photo</b> <small>(Case/500)</small></td><td class="price"><b>$69</b>/case</td></tr>
    <tr><td><b>Top-Load 6x4 Side Load Photo</b> <small>(Case/500)</small></td><td class="price"><b>$69</b>/case</td></tr>
    <tr><td><b>Top-Load 5x7 Photo</b> <small>(Case/500)</small></td><td class="price"><b>$95</b>/case</td></tr>
    <tr><td><b>Top-Load 6x9 Photo</b> <small>(Case/250)</small></td><td class="price"><b>$65</b>/case</td></tr>
    <tr><td><b>Top-Load Ticket (3⅜”x 7¼”)</b> <small>(Case/500)</small></td><td class="price"><b>$89</b>/case</td></tr>
    <tr><td><b>Top-Load Reg. Currency</b> <small>(Case/500)</small></td><td class="price"><b>$65</b>/case</td></tr>
    <tr><td><b>Top-Load Large Currency</b> <small>(Case/250)</small></td><td class="price"><b>$38</b>/case</td></tr>
    <tr><td><b>Top-Load 8x10 Photo</b> <small>(Case/250)</small></td><td class="price"><b>$99</b>/case</td></tr>
    <tr><td><b>Top-Load 8.5x11 Photo/Document</b> <small>(Case/250)</small></td><td class="price"><b>$109</b>/case</td></tr>
    <tr><td><b>Top-Load Thick Magazine 7mm</b> <small>(Case/50)</small></td><td class="price"><b>$49</b>/case</td></tr>
    <tr><td><b>Top-Load Super Thick Mag 10mm</b> <small>(Case/50)</small></td><td class="price"><b>$59</b>/case</td></tr>
    <tr><td><b>Top-Load 11x14 Photo</b> <small>(Case/100)</small></td><td class="price"><b>$79</b>/case</td></tr>
    <tr><td><b>Top-Load 11x17 Photo</b> <small>(Case/100)</small></td><td class="price"><b>$95</b>/case</td></tr>
    <tr><td><b>Top-Load 16x20 Photo</b> <small>(Case/50)</small></td><td class="price"><b>$79</b>/case</td></tr>
    <tr><td><b>Top-Load Pennant</b> <small>(Case/50)</small></td><td class="price"><b>$89</b>/case</td></tr>
    <tr><td><b>Top-Load 24x36 Poster</b> <small>(Case/10)</small></td><td class="price"><b>$49</b>/case</td></tr>
    <tr><td><b>Top-Load 29x43 Poster/Sheet</b> <small>(Case/10)</small></td><td class="price"><b>$65</b>/case</td></tr>
    <tr><td><b>Soft Card Sleeves</b> <small>(Case/10,000/100 packs)</small></td><td class="price"><b>$32</b>/case</td></tr>
    <tr><td><b>Thick Card Soft Sleeves</b> <small>(Case/10,000)</small></td><td class="price"><b>$45</b>/case</td></tr>
    <tr><td><b>Team Set Bags Resealable</b> <small>(Case/5,000/50 packs)</small></td><td class="price"><b>$62</b>/case</td></tr>
    <tr><td><b>Graded Bags Resealable</b> <small>(Case/5,000/50 packs)</small></td><td class="price"><b>$65</b>/case</td></tr>
    <tr><td><b>Postcard Soft Sleeves</b> <small>(Case/5,000/50 packs)</small></td><td class="price"><b>$49</b>/case</td></tr>
    <tr><td><b>4x6 Photo Soft Sleeves</b> <small>(Case/5,000/50 packs)</small></td><td class="price"><b>$59</b>/case</td></tr>
    <tr><td><b>5x7 Photo Soft Sleeves</b> <small>(Case/5,000/50 packs)</small></td><td class="price"><b>$69</b>/case</td></tr>
    <tr><td><b>8x10 Photo Soft Sleeves</b> <small>(Case/1,000/10 packs)</small></td><td class="price"><b>$35</b>/case</td></tr>
  </table>
</section>

<section class="sheet sheet-back">
  <div class="product-shot shot-ball" role="img" aria-label="Baseball in a clear acrylic cube"></div>
  <div class="product-shot shot-basketball" role="img" aria-label="Basketball in a clear acrylic display case"></div>
  <div class="brand">PAPER FINCH</div>
  <div class="product-shot shot-sleeves" role="img" aria-label="Packs of card holders and soft sleeves"></div>

  <table class="price-table back-top">
    <tr><th>Description</th><th class="price">Price</th></tr>
    <tr><td><b>Card Keeper 1</b> <small>(Case/2,000-10 200 Count Display Boxes)</small></td><td class="price"><b>$87.50</b>/case</td></tr>
    <tr><td><b>Card Keeper 2</b> <small>(Case/2,000-10 200 Count Display Boxes)</small></td><td class="price"><b>$65</b>/case</td></tr>
    <tr><td><b>Card Keeper 3</b> <small>(Case/1,000-10 100 Count Packages)</small></td><td class="price"><b>$79</b>/case</td></tr>
    <tr><td><b>Card Keeper 4</b> <small>(Case/1,000-10 100 Count Packages)</small></td><td class="price"><b>$125</b>/case</td></tr>
    <tr><td><b>Card Keeper 5</b> <small>(Case/1,000-10 100 Count Packages)</small></td><td class="price"><b>$110</b>/case</td></tr>
  </table>

  <table class="price-table bills">
    <tr><td>BS-RG &nbsp;<b>Bill Keeper 1 Regular Currency</b> <small>(Case/500)</small></td><td class="price"><b>$35</b>/case</td></tr>
    <tr><td>BS-LG &nbsp;<b>Bill Keeper 2 Large Currency</b> <small>(Case/500)</small></td><td class="price"><b>$40</b>/case</td></tr>
  </table>

  <table class="price-table cases">
    <tr><th colspan="3">DELUXE ACRYLIC SPORTS DISPLAY CASES</th></tr>
    <tr><td class="code">PG1</td><td><b>Deluxe Acrylic Football Case</b> <small>w/ Gold Risers &amp; Mirrored Back</small></td><td class="price"><b>$27</b> each</td></tr>
    <tr><td class="code">PG1-wm</td><td>Above <small>Wall Mount Version</small></td><td class="price"><b>$29</b> each</td></tr>
    <tr><td class="code">PG2</td><td><b>Deluxe Acrylic FS Helmet Case</b> <small>w/ Gold Risers &amp; Mirrored Back</small></td><td class="price"><b>$39</b> each</td></tr>
    <tr><td class="code">PG3</td><td><b>Deluxe Acrylic Mini Helmet Case</b> <small>w/ Gold Risers &amp; Mirror Back</small></td><td class="price"><b>$15</b> each</td></tr>
    <tr><td class="code">PG3-wm</td><td>Above <small>Wall Mount Version</small></td><td class="price"><b>$16</b> each</td></tr>
    <tr><td class="code">PG4</td><td><b>Deluxe Acrylic Basketball Case</b> <small>w/ Gold Risers &amp; Mirror Back</small></td><td class="price"><b>$37.50</b> each</td></tr>
    <tr><td class="code">PG5</td><td><b>“Golden Mitt” Baseball Display</b> <small>w/ Black Acrylic Base, Case/6</small></td><td class="price"><b>$7.50</b> each</td></tr>
    <tr><td class="code">PG6</td><td><b>Deluxe Acrylic Cap/Hat Case</b> <small>w/ Gold Risers &amp; Mirrored Back</small></td><td class="price"><b>$24</b> each</td></tr>
    <tr><td class="code">PG6-wm</td><td>Above <small>Wall Mount Version</small></td><td class="price"><b>$25</b> each</td></tr>
    <tr><td class="code">PG7</td><td><b>Deluxe Acrylic Baseball Bat Case</b> <small>(Wall Mount or Table Top)</small></td><td class="price"><b>$59</b> each</td></tr>
  </table>

  <div class="terms">
    <b><span class="label">TERMS of SALE:</span> All prices include shipping to a commercial/business address via Swift Parcel Ground.<br>
    Minimum order is $500. &nbsp;There is a $29 surcharge for residential delivery.</b><br>
    No additional charge for credit cards or PayWise. To order, please call or email.<br>
    All orders will be confirmed by Invoice via email.
  </div>

  <div class="company">
    <div class="company-name">PAPER FINCH, Inc.</div>
    <div class="company-line">14 Heron Lane • Maple Bluff CA</div>
    <div class="company-line">92601-4410 • 1-800-555-0142 • sales@paperfinch.com</div>
    <div class="company-line">paperfinch.com</div>
  </div>

  <div class="payment-band">
    <div class="pay-badge">PayWise</div>
    <div class="pay-badge">Vista</div>
    <div class="pay-badge">Meridian</div>
    <div class="pay-badge">Roamer</div>
    <div class="pay-badge">Amerifold</div>
  </div>

  <p class="ship-note">All orders ship from our warehouse in Cedar Falls, WA 98601</p>
  <p class="fine-print">Paper Finch, Card Keeper, &amp; Bill Keeper are trademarks of Paper Finch, Inc. © 2013, Paper Finch, Inc.</p>
</section>

</body>
</html>
```